Clone https://brinwexo.com (fully functional wordpress site with wooCommerce)

1) Clone or recreate the site in WordPress Woocomerece
2) Connect to our existing stripe account.
3) Make our text only changes (not style changes or anything complex.

We will provide all graphics and content to be copied and pasted in place of the existing text / graphics.

Please do not submit a design only. Thanks in advance.

Target Market(s)

Wordpress developer

Number of Pages Required

5+ page

Font styles to use
Sans Serif

Colors
acd036
9bcb3c
cadf82
eaf2ce

Requirements
Must have
• Fully functional wordpress site with Woo Comerece pluged in.
Should not have
• Design only

```html
<!DOCTYPE html>
<html lang="en">
<head>
<meta charset="utf-8">
<title>Brinwexo – Answering Services Overview</title>
<link rel="stylesheet" href="https://fonts.googleapis.com/css2?family=Open+Sans:wght@300;400;600;700&display=swap">
<style>
:root{
  --green-dark:#4b7a26;
  --green:#9bcb3c;
  --green-bright:#acd036;
  --green-pale:#cadf82;
  --green-mist:#eaf2ce;
  --green-footer:#3e6a22;
  --green-bottom:#2d4f18;
  --teal:#2f8f8a;
  --blue:#2a7ab8;
  --ink:#333;
  --muted:#777;
  --line:#d8d8d8;
  --white:#fff;
}
*{box-sizing:border-box;margin:0;padding:0}
html,body{width:1200px;height:5322px;overflow:hidden}
body{font-family:"Open Sans",Arial,sans-serif;color:var(--ink);background:var(--white);position:relative}
section,header,footer{position:absolute;left:0;width:1200px}
h1,h2,h3{font-weight:400}
.abs{position:absolute}

/* hero */
.hero{top:0;height:612px}
.hero-photo{position:absolute;inset:0;background:linear-gradient(100deg,#f3efe9 0%,#e8ddd2 35%,#d9c3b1 60%,#bfa592 80%,#e6dfd8 100%)}
.hero-shade{position:absolute;inset:0;background:rgba(40,40,40,.28)}
.site-nav{position:absolute;top:26px;left:0;width:1200px;height:40px}
.brand{position:absolute;left:60px;top:8px;font-size:24px;font-weight:700;color:var(--white);display:flex;align-items:center;gap:8px}
.brand-dot{width:18px;height:18px;border-radius:50%;background:var(--green-bright)}
.menu{position:absolute;right:80px;top:16px;display:flex;gap:22px;font-size:15px;color:var(--white);list-style:none}
.menu .active{color:var(--green-bright)}
.search{position:absolute;right:54px;top:16px}
.hero-title{position:absolute;top:274px;width:100%;text-align:center;color:var(--white);font-size:30px}
.hero-sub{position:absolute;top:316px;width:100%;text-align:center;color:var(--white);font-size:14px}
.btn-ghost{display:inline-block;border:2px solid var(--white);color:var(--white);font-size:17px;padding:9px 0;border-radius:3px;white-space:nowrap;text-align:center}
.hero .btn-ghost{position:absolute;top:398px;left:470px;width:260px}

/* section headings */
.heading-rule{position:absolute;width:100%;display:flex;align-items:center;justify-content:center;gap:30px;font-size:26px;color:#444}
.heading-rule::before,.heading-rule::after{content:"";width:210px;height:2px;background:var(--line)}

/* process */
.flow-step{position:absolute;width:220px;text-align:center;font-size:14px;color:var(--teal);line-height:1.35}
.flow-icon{width:110px;height:110px;border-radius:50%;border:3px solid currentColor;margin:0 auto 12px;display:flex;align-items:center;justify-content:center;background:var(--white)}

/* service boxes */
.service-box{position:absolute;left:120px;width:960px;border-radius:10px;color:var(--white)}
.service-box.dark{background:var(--green-dark)}
.service-box.light{background:var(--green)}
.box-title{position:absolute;width:100%;text-align:center;font-size:27px}
.service{position:absolute;width:260px;text-align:center;font-size:15px}
.service svg{display:block;margin:0 auto 14px}
.btn-small{position:absolute;left:410px;width:140px;text-align:center;border:2px solid var(--white);border-radius:4px;font-size:13px;padding:6px 0;color:var(--white)}

/* team panel */
.team-band{top:2336px;height:451px;background:var(--green-pale)}
.team-panel{position:absolute;left:120px;top:78px;width:960px;height:302px;background:var(--white);box-shadow:0 1px 3px rgba(0,0,0,.1)}
.tabs{position:absolute;left:0;top:0;display:flex}
.tab{width:152px;height:30px;line-height:30px;text-align:center;font-size:12px;background:#eee;border-right:1px solid #ddd;color:#555}
.tab.active{background:var(--white);color:#222;font-weight:600}
.tab-line{position:absolute;left:0;top:30px;width:960px;height:1px;background:#ddd}
.avatar{position:absolute;border-radius:50%;background:linear-gradient(150deg,#d9b48c,#a8744d);border:4px solid var(--white);box-shadow:0 0 0 2px #ccc}
.team-name{position:absolute;left:330px;top:60px;font-size:13px;color:#555}
.bullets{position:absolute;list-style:none;font-size:12px;line-height:22px;color:#444}
.bullets li::before{content:"• ";color:var(--green)}

/* story */
.story{top:2840px;height:410px}
.big-num{position:absolute;left:120px;top:0;font-size:60px;color:var(--green-dark);font-weight:300;line-height:1}
.big-num small{font-size:26px;color:#333}
.story-sub{position:absolute;left:120px;top:62px;font-size:26px;color:#333}
.story-text{position:absolute;font-size:13px;line-height:20px;color:#555}
.phone-shot{position:absolute;left:455px;top:-20px;width:290px;height:430px;border-radius:30px;background:linear-gradient(160deg,#3a3a3a,#111 60%,#c9a387 90%)}
.quality-title{position:absolute;left:795px;top:0;font-size:50px;color:var(--green-dark);line-height:1}
.quality-sub{position:absolute;left:795px;top:62px;font-size:26px;color:#333}

/* specialist */
.specialist{top:3255px;height:365px;background:var(--green)}
.spec-text{position:absolute;left:180px;top:112px;width:840px;text-align:center;font-size:12px;line-height:18px;color:#2c3a14}
.spec-meet{position:absolute;top:160px;width:100%;text-align:center;font-size:16px;font-weight:600;color:#2c3a14}

/* steps */
.steps{top:3640px;height:1080px}
.step-title{position:absolute;font-size:28px;color:#333}
.step-title b{color:var(--green-dark);font-weight:400}
.step-text{position:absolute;font-size:13px;line-height:20px;color:#555}
.step-art{position:absolute;border-radius:6px;background:linear-gradient(135deg,#f4f6f8,#e3e8ec)}

/* cta */
.cta{top:4721px;height:292px}
.cta-photo{position:absolute;inset:0;background:linear-gradient(90deg,#6b4a33 0%,#a27b5d 28%,#d9d4cf 55%,#b8b3ad 80%,#8a8580 100%)}
.cta-shade{position:absolute;inset:0;background:rgba(30,30,30,.25)}
.cta-title{position:absolute;left:470px;top:92px;font-size:30px;color:var(--white)}
.cta-sub{position:absolute;left:470px;top:135px;width:330px;font-size:13px;color:var(--white);line-height:18px}
.cta .btn-ghost{position:absolute;left:465px;top:190px;width:280px}

/* footer */
.site-footer{top:5013px;height:259px;background:var(--green-footer);color:var(--white)}
.footer-mark{position:absolute;left:110px;top:80px;width:120px;height:120px;border-radius:50%;background:rgba(255,255,255,.06)}
.footer-links{position:absolute;top:68px;list-style:none;font-size:14px;line-height:24px}
.footer-links li::before{content:"• "}
.bottom-bar{top:5272px;height:50px;background:var(--green-bottom);color:var(--white);font-size:12px}
.bottom-bar p{position:absolute;left:120px;top:17px}
.social{position:absolute;right:120px;top:19px;display:flex;gap:18px}
.social span{width:12px;height:12px;border-radius:50%;background:var(--white);opacity:.9}
</style>
</head>
<body>

<header class="hero">
  <div class="hero-photo" role="img" aria-label="Photo of a smiling call agent wearing a headset"></div>
  <div class="hero-shade"></div>
  <nav class="site-nav">
    <div class="brand"><span class="brand-dot"></span>Brinwexo</div>
    <ul class="menu">
      <li>Home</li><li class="active">Services</li><li>Pricing</li><li>About</li><li>Contact Us</li><li>Login</li><li>Free Trial</li>
    </ul>
    <svg class="search" width="16" height="16" viewBox="0 0 16 16"><circle cx="6.5" cy="6.5" r="5" fill="none" stroke="#fff" stroke-width="2"/><path d="M10 10l5 5" stroke="#fff" stroke-width="2"/></svg>
  </nav>
  <h1 class="hero-title">Answering Services Overview</h1>
  <p class="hero-sub">Great callers talk to friendly and helpful agents who always know how to help</p>
  <span class="btn-ghost">Try Free Trial for 14 days</span>
</header>

<section class="how" style="top:612px;height:1100px">
  <h2 class="heading-rule" style="top:52px">How our services work</h2>
  <div class="abs" style="left:1078px;top:130px;width:2px;height:190px;background:var(--line)"></div>
  <div class="flow-step" style="left:100px;top:120px">
    <div class="flow-icon"><svg width="46" height="46" viewBox="0 0 24 24" fill="none" stroke="currentColor" stroke-width="1.5"><path d="M5 3h4l2 5-3 2a12 12 0 0 0 6 6l2-3 5 2v4a2 2 0 0 1-2 2A18 18 0 0 1 3 5a2 2 0 0 1 2-2z"/></svg></div>
    Customer places call<br>to your business
  </div>
  <div class="flow-step" style="left:410px;top:120px">
    <div class="flow-icon"><svg width="48" height="48" viewBox="0 0 24 24" fill="none" stroke="currentColor" stroke-width="1.5"><path d="M3 9l2-5h14l2 5M3 9h18v2a3 3 0 0 1-6 0 3 3 0 0 1-6 0 3 3 0 0 1-6 0zM5 13v8h14v-8M10 21v-5h4v5"/></svg></div>
    Brinwexo answers<br>as your business
  </div>
  <div class="flow-step" style="left:720px;top:120px;color:#333">
    <div class="flow-icon"><svg width="48" height="48" viewBox="0 0 24 24" fill="none" stroke="currentColor" stroke-width="1.5"><path d="M4 14v-2a8 8 0 0 1 16 0v2M4 14h3v5H4zM17 14h3v5h-3zM20 19c0 2-3 2-6 2"/></svg></div>
    Brinwexo agent<br>follows your script
  </div>

  <div class="service-box dark" style="top:348px;height:726px">
    <h3 class="box-title" style="top:36px">Answering Services</h3>
    <div class="service" style="left:40px;top:90px"><svg width="40" height="40" viewBox="0 0 24 24" fill="none" stroke="#fff" stroke-width="1.5"><path d="M4 4h12l4 4v12H4zM8 4v16"/></svg>Message Taking</div>
    <div class="service" style="left:350px;top:90px"><svg width="40" height="40" viewBox="0 0 24 24" fill="none" stroke="#fff" stroke-width="1.5"><rect x="3" y="4" width="18" height="16" rx="1"/><circle cx="9" cy="11" r="2"/><path d="M6 16c1-2 5-2 6 0M14 9h4M14 12h4"/></svg>Lead Collection</div>
    <div class="service" style="left:660px;top:90px"><svg width="40" height="40" viewBox="0 0 24 24" fill="none" stroke="#fff" stroke-width="1.5"><rect x="3" y="5" width="18" height="16" rx="1"/><path d="M3 9h18M8 3v4M16 3v4M7 13h2M11 13h2M15 13h2M7 17h2M11 17h2"/></svg>Appointment Scheduling</div>
    <div class="service" style="left:40px;top:264px"><svg width="40" height="40" viewBox="0 0 24 24" fill="none" stroke="#fff" stroke-width="1.5"><rect x="3" y="6" width="18" height="12" rx="1"/><path d="M3 10h18M6 15h4"/></svg>Order Processing</div>
    <div class="service" style="left:350px;top:264px"><svg width="40" height="40" viewBox="0 0 24 24" fill="none" stroke="#fff" stroke-width="1.5"><circle cx="12" cy="12" r="9"/><path d="M12 7v5l3 2"/></svg>After Hours Support</div>
    <div class="service" style="left:660px;top:264px"><svg width="40" height="40" viewBox="0 0 24 24" fill="none" stroke="#fff" stroke-width="1.5"><path d="M5 3h4l2 5-3 2a12 12 0 0 0 6 6l2-3 5 2v4a2 2 0 0 1-2 2A18 18 0 0 1 3 5a2 2 0 0 1 2-2zM15 3h6v6"/></svg>Overflow Support</div>
    <div class="service" style="left:40px;top:464px"><svg width="40" height="40" viewBox="0 0 24 24" fill="none" stroke="#fff" stroke-width="1.5"><path d="M3 4h18v12H9l-5 4v-4H3z"/><path d="M7 8h10M7 11h7"/></svg>Emergency Response</div>
    <div class="service" style="left:350px;top:464px"><svg width="40" height="40" viewBox="0 0 24 24" fill="none" stroke="#fff" stroke-width="1.5"><path d="M5 3h4l2 5-3 2a12 12 0 0 0 6 6l2-3 5 2v4a2 2 0 0 1-2 2A18 18 0 0 1 3 5a2 2 0 0 1 2-2zM14 4l6 6M20 4l-6 6"/></svg>Call Transfers</div>
    <div class="service" style="left:660px;top:464px"><svg width="40" height="40" viewBox="0 0 24 24" fill="none" stroke="#fff" stroke-width="1.5"><path d="M3 8h8v6H6l-3 2zM13 10h8v6h-1v2l-3-2h-4z"/></svg>Bilingual Services</div>
    <span class="btn-small" style="top:654px">Learn More</span>
  </div>

  <div class="service-box light" style="top:1103px;height:295px">
    <h3 class="box-title" style="top:28px">Call Center Services</h3>
    <div class="service" style="left:40px;top:88px"><svg width="40" height="40" viewBox="0 0 24 24" fill="none" stroke="#fff" stroke-width="1.5"><rect x="3" y="4" width="18" height="16" rx="1"/><circle cx="9" cy="11" r="2"/><path d="M6 16c1-2 5-2 6 0M14 9h4M14 12h4M14 15h3"/></svg>Dedicated Account Manager</div>
    <div class="service" style="left:350px;top:88px"><svg width="40" height="40" viewBox="0 0 24 24" fill="none" stroke="#fff" stroke-width="1.5"><circle cx="8" cy="8" r="3"/><circle cx="16" cy="8" r="3"/><path d="M2 19c1-4 11-4 12 0M10 19c1-4 11-4 12 0"/></svg>Specialized Agent Training</div>
    <div class="service" style="left:660px;top:88px"><svg width="40" height="40" viewBox="0 0 24 24" fill="none" stroke="#fff" stroke-width="1.5"><rect x="4" y="4" width="16" height="11" rx="1"/><path d="M2 18h20M8 12l3-3 2 2 3-3"/></svg>Monthly Performance Calls</div>
    <span class="btn-small" style="top:224px">Learn More</span>
  </div>
</section>

<section class="deliver" style="top:2060px;height:250px">
  <div class="abs" style="left:120px;top:30px;width:960px;height:2px;background:var(--line)"></div>
  <div class="abs" style="left:120px;top:30px;width:2px;height:150px;background:var(--line)"></div>
  <div class="flow-step" style="left:200px;top:42px">
    <div class="flow-icon" style="width:104px;height:104px"><svg width="46" height="46" viewBox="0 0 24 24" fill="none" stroke="currentColor" stroke-width="1.5"><rect x="3" y="4" width="14" height="16" rx="1"/><path d="M6 9h8M6 12h8M6 15h5"/><circle cx="17" cy="16" r="3.5"/><path d="M19.5 18.5L22 21"/></svg></div>
    Brinwexo captures call<br>summary information
  </div>
  <div class="flow-step" style="left:485px;top:42px;color:var(--blue)">
    <div class="flow-icon" style="width:104px;height:104px"><svg width="46" height="46" viewBox="0 0 24 24" fill="none" stroke="currentColor" stroke-width="1.5"><rect x="3" y="5" width="18" height="13" rx="1"/><path d="M3 6l9 7 9-7"/><circle cx="12" cy="19" r="2.5"/></svg></div>
    Brinwexo delivers call<br>summary to your inbox
  </div>
  <div class="flow-step" style="left:780px;top:42px;color:#333">
    <div class="flow-icon" style="width:104px;height:104px"><svg width="48" height="48" viewBox="0 0 24 24" fill="none" stroke="currentColor" stroke-width="1.5"><path d="M2 11l4-3 4 1 3-2 4 2 5 2M6 8l-3 6 4 4 2-1 2 2 2-1 2 1 4-4M9 13l2 2M11 12l3 3"/></svg></div>
    Done!
  </div>
</section>

<section class="team-band">
  <div class="team-panel">
    <div class="tabs">
      <div class="tab active">Message Taking</div><div class="tab">Message Taking</div><div class="tab">Message Taking</div><div class="tab">Message Taking</div>
    </div>
    <div class="tab-line"></div>
    <div class="avatar" style="left:26px;top:48px;width:128px;height:128px" role="img" aria-label="Portrait photo of a customer support agent"></div>
    <p class="team-name">Dana Whitfield  |  Customer Support  |  Team Member Since 2014</p>
    <ul class="bullets" style="left:30px;top:222px"><li>100% of agents located in the USA</li><li>Bilingual services in English &amp; Spanish</li></ul>
    <ul class="bullets" style="left:330px;top:222px"><li>Customizable agent scripts</li><li>Customizable call forwarding</li></ul>
    <ul class="bullets" style="left:630px;top:222px"><li>Real-time message to email</li><li>Flexible message delivery options</li></ul>
  </div>
</section>

<section class="story">
  <div class="big-num">27<small>Years of</small></div>
  <div class="story-sub">Experience</div>
  <p class="story-text" style="left:120px;top:112px;width:300px">Brinwexo was founded in 1990 when we started up with just 5 employees and our first 25 customers. In the 27 years since, Brinwexo has grown to a team of over 125 and supports thousands of businesses across the country. With decades of experience working with just about every industry, our agents have the know-how needed to deliver truly superior service on every call.</p>
  <div class="phone-shot" role="img" aria-label="Photo of a hand holding a smartphone showing the app"></div>
  <div class="quality-title">Highest</div>
  <div class="quality-sub">Quality Standards</div>
  <p class="story-text" style="left:795px;top:112px;width:290px">Our agents are the best in the industry because we care about quality from the very start. We hire less than 5% of our applicants after a rigorous screening process, spend weeks with them in training, and then give them a dedicated coach to monitor and ensure awesome performance. 100% of our calls are recorded, which we use to make sure our agents give great, consistent service around the clock.</p>
</section>

<section class="specialist">
  <p class="spec-text">Marcus joined Brinwexo in 2014 as a customer care representative. He is an expert at answering new customer questions, and always provides an exceptional customer experience. Prior to joining Brinwexo, Marcus was an account manager for a national retail service.</p>
  <p class="spec-meet">Meet Marcus, one of our awesome Product Specialists!</p>
  <div class="avatar" style="left:560px;top:200px;width:80px;height:80px;background:linear-gradient(150deg,#e5d8cc,#8a6a55)" role="img" aria-label="Portrait photo of a product specialist"></div>
</section>

<section class="steps">
  <h2 class="heading-rule" style="top:38px">It's easy to get started</h2>

  <div class="step-art" style="left:110px;top:230px;width:300px;height:200px" role="img" aria-label="Illustration of a phone number picker screen"></div>
  <h3 class="step-title" style="left:456px;top:198px"><b>1</b> Get a Number, or Forward Yours To Us</h3>
  <p class="step-text" style="left:456px;top:244px;width:600px">When you signup for services we'll provide you with a phone number in your choice of local city or toll-free prefix. If you already have a number that you want to continue using that works too. You can either forward the calls to your Brinwexo number, or you can permanently port the number to reside on our platform.</p>

  <h3 class="step-title" style="left:120px;top:505px"><b>2</b> Configure Your Custom Call Flow</h3>
  <p class="step-text" style="left:120px;top:550px;width:600px">Our agents can do as little or as much as you'd like when we answer your calls. When you setup service, a script consultant will talk with you to understand how you'd like for us to handle your calls, and we'll setup a custom call flow for our agents to follow. Whether you need us to take messages, collect leads, receive orders, register event attendees, or act as your virtual receptionist, our team will put together a script that gives you exactly what you need.</p>
  <div class="step-art" style="left:790px;top:520px;width:290px;height:220px" role="img" aria-label="Illustration of a custom call flow diagram"></div>

  <div class="step-art" style="left:110px;top:790px;width:270px;height:210px" role="img" aria-label="Illustration of a recent call summary card"></div>
  <h3 class="step-title" style="left:456px;top:797px"><b>3</b> Receive a Call Summary for Every Call</h3>
  <p class="step-text" style="left:456px;top:842px;width:600px">When we begin answering your calls (24 hours after script setup), we'll follow the call flow you designed and send you the corresponding message, lead, order, etc. within minutes of call completion.</p>
</section>

<section class="cta">
  <div class="cta-photo" role="img" aria-label="Photo of a smiling support agent wearing a headset in an office"></div>
  <div class="cta-shade"></div>
  <h2 class="cta-title">Start your free trial today</h2>
  <p class="cta-sub">Try Brinwexo free for 14 days. We can fill up to 50 calls for your business, no credit card required.</p>
  <span class="btn-ghost">Start Free Trial for 14 Days !</span>
</section>

<footer class="site-footer">
  <div class="footer-mark"></div>
  <ul class="footer-links" style="left:378px"><li>Services</li><li>Blog</li><li>FAQ</li></ul>
  <ul class="footer-links" style="left:628px"><li>Services</li><li>Blog</li><li>FAQ</li></ul>
  <ul class="footer-links" style="left:880px"><li>Services</li><li>Blog</li><li>FAQ</li></ul>
</footer>
<section class="bottom-bar">
  <p>© Brinwexo, Inc 2017. All rights reserved. <b>Privacy Policy</b> | <b>Terms of Service</b></p>
  <div class="social"><span></span><span></span><span></span><span></span></div>
</section>

</body>
</html>
```